Boutique Jewellery Card [UPDATED] Embossing and Foil

Hi Designers,

What will win you this competition is your input on making my card look very professional and classy

Just some overview information.

I am striving to be the most prestigious jeweller going around specialising in custom designed jewellery, engagement rings and repairs on a bigger budget.

I am spending a lot on the printing including thick cards, rounded corners, multi level embossing and foiling.

Front:

I want my entire logo on the front, which I will have embossed and foiled (source file included)
Optional: I also want a lower embossing of a repeating pattern which I am not sure on. I need YOUR input here

Back:

I need you to use your skills and experience to make my details look very important, professional and classy.

The details I need on the back are:

Marcus Feldwright
Your Jewellery Stylist

www.marcusfeldwright.com
0492 836 514
marcus@marcusfeldwright.com

The font MUST match the font/style used in the logo.
Everything else including layout, whether my logo is on the back etc, engrave/endent, foiling etc is what I need your input for
Updates

Project Deadline Extended Reason: I was a bit slow and out of action at the start, but we're almost there, just need a few more days to finalize Added Sunday, November 16, 2014

Target Market(s)

25 - 80 year olds. Fashion concious. Wealthy

Industry/Entity Type

Printing

Contact Information for Business Card

Marcus Feldwright
Your Jewellery Stylist

0492 836 514
marcus@marcusfeldwright.com
www.marcusfeldwright.com
- facebook and instagram logo's

Requirements
Must have
• Must use the font from my logo on the back, or very similar
• My logo on the front
• My details on the back must be the centre of attention, my logo can still be there but is less important.
• Back must include the facebook and instagram logo's
Nice to have
• repeating pattern or monogram

```html
<!DOCTYPE html>
<html lang="en">
<head>
<meta charset="utf-8">
<title>Marcus Feldwright – Jewellery Stylist Cards</title>
<link rel="stylesheet" href="https://fonts.googleapis.com/css2?family=Open+Sans:wght@400;600&family=Raleway:wght@400;500&display=swap">
<style>
  :root {
    --backdrop: #d8d5cf;
    --card: #ebe8e3;
    --card-edge: #dcd8d1;
    --ink: #3a3a3a;
    --ink-soft: #555555;
    --band: #262626;
    --band-text: #f2f2f2;
    --ring: #1f1f1f;
  }
  * { margin: 0; padding: 0; box-sizing: border-box; }
  html, body { width: 1070px; height: 1200px; overflow: hidden; }
  body {
    background: var(--backdrop);
    position: relative;
    font-family: "Open Sans", Arial, sans-serif;
    color: var(--ink);
  }
  .card {
    position: absolute;
    background: var(--card);
    border: 1px solid var(--card-edge);
    box-shadow: 0 6px 20px rgba(0,0,0,0.08);
    overflow: hidden;
  }
  .card--front {
    left: 141px; top: 112px;
    width: 640px; height: 459px;
    border-radius: 0 230px 230px 0;
  }
  .card--back {
    left: 168px; top: 683px;
    width: 824px; height: 470px;
    border-radius: 235px 0 0 235px;
  }
  .band { position: absolute; background: var(--band); }
  .card--front .band { left: 0; top: 152px; width: 420px; height: 99px; }
  .card--back .band { left: 300px; top: 145px; width: 524px; height: 105px; }
  .ring {
    position: absolute;
    width: 214px; height: 214px;
    border: 26px solid var(--ring);
    border-radius: 50%;
  }
  .card--front .ring { left: 352px; top: 132px; }
  .card--back .ring { left: 112px; top: 94px; }
  .holder-name {
    position: absolute; left: 38px; top: 44px;
    font-size: 28px; font-weight: 600; color: var(--ink);
  }
  .holder-role {
    position: absolute; left: 38px; top: 92px;
    font-size: 20px; color: var(--ink-soft);
  }
  .band-name {
    position: absolute; left: 24px; top: 186px;
    font-family: "Raleway", Arial, sans-serif;
    font-weight: 400; font-size: 22px; line-height: 1;
    letter-spacing: 2px; color: var(--band-text);
    white-space: nowrap;
  }
  .contact-list {
    position: absolute; left: 42px; top: 346px;
    list-style: none;
    font-size: 16px; color: var(--ink-soft);
  }
  .contact-list li { display: flex; align-items: center; gap: 14px; height: 32px; }
  .contact-list svg { width: 16px; height: 16px; fill: var(--ink-soft); }
  .back-web {
    position: absolute; right: 34px; top: 213px;
    font-size: 18px; letter-spacing: 2px; color: var(--band-text);
    white-space: nowrap;
  }
  .back-web strong { font-weight: 600; }
  .show-through {
    position: absolute; right: 90px;
    transform: scaleX(-1);
    opacity: 0.3;
    color: var(--ink);
    white-space: nowrap;
  }
  .show-through--head { top: 40px; }
  .show-through--head .holder-name,
  .show-through--head .holder-role { position: static; }
  .show-through--head .holder-role { margin-top: 10px; }
  .show-through--contacts { top: 330px; }
  .show-through--contacts .contact-list { position: static; }
</style>
</head>
<body>
  <section class="card card--front" aria-label="Card side with contact details">
    <p class="holder-name">Marcus Feldwright</p>
    <p class="holder-role">Jewellery Stylist</p>
    <div class="band" role="img" aria-label="Dark band with faint repeating emboss pattern"></div>
    <p class="band-name">MARCUS FELDWRIGHT</p>
    <div class="ring"></div>
    <ul class="contact-list">
      <li>
        <svg viewBox="0 0 16 16" aria-hidden="true"><circle cx="8" cy="8" r="8"/><path d="M5 4h2l1 2-1 1a5 5 0 0 0 2 2l1-1 2 1v2a1 1 0 0 1-1 1A7 7 0 0 1 4 5a1 1 0 0 1 1-1z" fill="#ebe8e3"/></svg>
        <span>0492 836 514</span>
      </li>
      <li>
        <svg viewBox="0 0 16 16" aria-hidden="true"><rect x="1" y="3" width="14" height="10" rx="1"/><path d="M1 4l7 5 7-5" stroke="#ebe8e3" stroke-width="1.4" fill="none"/></svg>
        <span>marcus@marcusfeldwright.com</span>
      </li>
      <li>
        <svg viewBox="0 0 16 16" aria-hidden="true"><rect x="1" y="11" width="3" height="3"/><rect x="6" y="8" width="3" height="6"/><rect x="11" y="4" width="3" height="10"/></svg>
        <span>www.marcusfeldwright.com</span>
      </li>
    </ul>
  </section>

  <section class="card card--back" aria-label="Card side with name band">
    <div class="show-through show-through--head" aria-hidden="true">
      <p class="holder-name">Marcus Feldwright</p>
      <p class="holder-role">Jewellery Stylist</p>
    </div>
    <div class="band" role="img" aria-label="Dark band with faint repeating emboss pattern"></div>
    <div class="ring"></div>
    <p class="back-web">www.<strong>MarcusFeldwright</strong>.com</p>
    <div class="show-through show-through--contacts" aria-hidden="true">
      <ul class="contact-list">
        <li>
          <svg viewBox="0 0 16 16"><circle cx="8" cy="8" r="8"/><path d="M5 4h2l1 2-1 1a5 5 0 0 0 2 2l1-1 2 1v2a1 1 0 0 1-1 1A7 7 0 0 1 4 5a1 1 0 0 1 1-1z" fill="#ebe8e3"/></svg>
          <span>0492 836 514</span>
        </li>
        <li>
          <svg viewBox="0 0 16 16"><rect x="1" y="3" width="14" height="10" rx="1"/><path d="M1 4l7 5 7-5" stroke="#ebe8e3" stroke-width="1.4" fill="none"/></svg>
          <span>marcus@marcusfeldwright.com</span>
        </li>
        <li>
          <svg viewBox="0 0 16 16"><rect x="1" y="11" width="3" height="3"/><rect x="6" y="8" width="3" height="6"/><rect x="11" y="4" width="3" height="10"/></svg>
          <span>www.marcusfeldwright.com</span>
        </li>
      </ul>
    </div>
  </section>
</body>
</html>
```